Belle Rive Weddings and Events

I am a small boutique wedding coordinator, stylist and bridal consultant/coach/assistant. I am based in Brisbane, Australia and my business is geared towards mid range- high end budget bridal couples.
I am after some business cards that are double sided, with the logo on one side and all other information on the other side, including the business tagline of design, create, celebrate. The look of the card needs to be clean and crisp, with white and the tones of grey of the logo.The final design needs to convey sophistication and poise. Perhaps the logo and tagline could be done in a metallic silver with the rest of the text in the shades of grey from the style guide attached below.
Title- Mira Tolvarenko - Director / Events Manager and Stylist
Address - 218 Halbrook Terrace, Wexley Vale, QLD, 4127
Phone- 07 3894 2167
Mobile- 0438 725 519
Email- Mira@bellerivecelebra.com.au
Website- www.bellerivecelebra.com.au

```html
<!DOCTYPE html>
<html lang="en">
<head>
<meta charset="utf-8">
<title>Belle Rive Weddings and Events – Business Card</title>
<link rel="stylesheet" href="https://fonts.googleapis.com/css2?family=Cormorant+Garamond:ital,wght@0,400;0,500;1,400;1,500&family=Italianno&display=swap">
<style>
  :root {
    --stage: #d9d9d9;
    --card: #f7f7f7;
    --band: #a3a3a3;
    --band-line: #8d8d8d;
    --silver: #9a9a9a;
    --ink: #4a4a4a;
    --ink-soft: #6e6e6e;
    --ornament-a: #d2d2d2;
    --ornament-b: #ececec;
  }
  * { margin: 0; padding: 0; box-sizing: border-box; }
  html, body {
    width: 1200px; height: 899px; overflow: hidden;
    background: var(--stage);
  }
  .sheet {
    width: 1200px; height: 899px;
    display: flex; flex-direction: column; align-items: center; justify-content: center;
    gap: 44px;
  }
  .card {
    position: relative;
    width: 720px; height: 400px;
    background: var(--card);
    box-shadow: 0 6px 18px rgba(0,0,0,.18);
    overflow: hidden;
  }
  .card-bands { position: absolute; inset: 0; }
  .logo {
    position: absolute; left: 250px; top: 60px;
    width: 220px; height: 170px;
    display: flex; flex-direction: column; align-items: center; justify-content: center;
    gap: 14px;
  }
  .logo-mark {
    width: 14px; height: 14px; border-radius: 50%;
    background: var(--silver);
  }
  .logo-name {
    font-family: "Cormorant Garamond", serif;
    font-weight: 500; font-size: 34px; line-height: 1.05;
    color: var(--silver); text-align: center;
  }
  .ornament {
    position: absolute;
    border-radius: 40px;
    background: radial-gradient(ellipse at center, var(--ornament-a), var(--ornament-b) 70%, transparent 100%);
  }
  .ornament-front { left: 300px; top: 238px; width: 120px; height: 46px; }
  .tagline {
    position: absolute; right: 60px; top: 312px;
    font-family: "Cormorant Garamond", serif; font-style: italic;
    font-size: 24px; letter-spacing: 4px;
    color: var(--silver);
  }
  .details {
    position: absolute; left: 170px; top: 96px; width: 400px;
    text-align: center;
    font-family: "Cormorant Garamond", serif; color: var(--ink-soft);
  }
  .person-name {
    font-family: "Italianno", cursive;
    font-size: 50px; line-height: 1; letter-spacing: 2px;
    color: var(--ink);
  }
  .person-title { font-style: italic; font-size: 16px; margin-top: 2px; }
  .rule {
    height: 1px; width: 360px; margin: 12px auto 12px;
    background: linear-gradient(90deg, transparent, var(--band), transparent);
  }
  .contact-line { font-size: 15px; line-height: 1.55; }
  .contact-line.italic { font-style: italic; }
  .ornament-back { left: 380px; top: 262px; width: 190px; height: 96px; }
</style>
</head>
<body>
<main class="sheet">

  <section class="card card-front" aria-label="Card front">
    <svg class="card-bands" width="720" height="400" viewBox="0 0 720 400" aria-hidden="true">
      <path d="M0 200 H120 Q88 270 120 340 H0 Z" fill="var(--band)"/>
      <rect x="128" y="200" width="4" height="140" fill="var(--band-line)"/>
      <path d="M720 40 H600 Q632 110 600 180 H720 Z" fill="var(--band)"/>
      <rect x="588" y="40" width="4" height="140" fill="var(--band-line)"/>
    </svg>
    <div class="logo">
      <span class="logo-mark"></span>
      <span class="logo-name">Belle Rive<br>Weddings and Events</span>
    </div>
    <div class="ornament ornament-front" role="img" aria-label="Silver filigree scroll ornament beneath the logo"></div>
    <p class="tagline">design, create, celebrate</p>
  </section>

  <section class="card card-back" aria-label="Card back">
    <svg class="card-bands" width="720" height="400" viewBox="0 0 720 400" aria-hidden="true">
      <path d="M0 220 H120 Q88 290 120 360 H0 Z" fill="var(--band)"/>
      <rect x="128" y="220" width="4" height="140" fill="var(--band-line)"/>
      <path d="M720 30 H600 Q632 100 600 170 H720 Z" fill="var(--band)"/>
      <rect x="588" y="30" width="4" height="140" fill="var(--band-line)"/>
    </svg>
    <div class="details">
      <h1 class="person-name">Mira Tolvarenko</h1>
      <p class="person-title">Director / Events Manager and Stylist</p>
      <div class="rule"></div>
      <p class="contact-line italic">218 Halbrook Terrace, Wexley Vale, QLD, 4127</p>
      <p class="contact-line">P: 07 3894 2167 | M: 0438 725 519 | E: Mira@bellerivecelebra.com.au</p>
      <p class="contact-line italic">www.bellerivecelebra.com.au</p>
    </div>
    <div class="ornament ornament-back" role="img" aria-label="Silver filigree swirl ornament with hanging pearl drop"></div>
  </section>

</main>
</body>
</html>
```